Corvane Partners Web Design

Dear all
I need a web design for a financial services site. We are a broker who deals with many different financial institutions and require a clean, simple and instantly impressive site based on the colour scheme that SketchGuild created for us. A landing page (www.crvnp.mx) gives an idea of the logo and clour scheme but we are looking at either a one page site with rollover text boxes or a 3 or 4 page site depending on the preference of the designer and the best user experience. The site“s purpose is to give confidence that the company exists rather than impart pages of information although we would like this to be a site that can expand over time as the company grows. For now the requirement is for a clear set of possibly changing images at the centre of a white screen that relate to finance in general nad the benefits of wealth creation as well as sectios either along the top or bottom - Our Company, Our Approach, Our services, Our clients, Contact (user to fill in contact box to be sent to info@crvnp.mx. The text for each of these boxes I assume can be added by the coding team here, it the overall look and feel that I am looking for from SketchGuild - deadline can be extended if necessary but I was hoping to wrap this all up in October

Target Market(s)

Succesful individuals looking to maximise returns on their investment via world class financial institutions and supported throughout by qualified independent financial advisors

Industry/Entity Type

Finance

Requirements
Must have
• Logo and color scheme of the logo design SketchGuild sent - I have all these sourcefiles, pantone and fonts

```html
<!DOCTYPE html>
<html lang="en">
<head>
<meta charset="utf-8">
<title>Corvane Partners</title>
<link rel="stylesheet" href="https://fonts.googleapis.com/css2?family=Josefin+Sans:wght@300;400&family=Archivo+Narrow:wght@700&family=Arimo:wght@700&display=swap">
<style>
  :root {
    --navy: #1d2f52;
    --orange: #f0a033;
    --white: #ffffff;
    --ink: #3a3f4a;
    --mist: #ebebeb;
    --sky-deep: #024a6e;
    --sky-mid: #0779a6;
    --sky-glow: #1fc4d9;
  }
  * { margin: 0; padding: 0; box-sizing: border-box; }
  html, body { width: 1200px; height: 901px; overflow: hidden; background: var(--white); }
  body { position: relative; font-family: "Josefin Sans", sans-serif; }

  .site-header { position: absolute; left: 0; top: 0; width: 1200px; height: 138px; background: var(--white); }
  .brand { position: absolute; left: 132px; top: 52px; display: flex; align-items: center; gap: 10px; }
  .brand-mark { width: 26px; height: 26px; border-radius: 50%; background: var(--navy); }
  .brand-name { font-family: "Josefin Sans", sans-serif; font-weight: 400; font-size: 17px; letter-spacing: 3px; color: var(--navy); text-transform: uppercase; line-height: 1.1; }

  .main-nav { position: absolute; top: 0; left: 0; width: 1200px; height: 138px; }
  .nav-item { position: absolute; top: 94px; font-size: 19px; font-weight: 400; letter-spacing: 1px; color: var(--ink); text-decoration: none; text-transform: uppercase; transform: translateX(-50%); white-space: nowrap; }
  .nav-item.is-active::after { content: ""; position: absolute; left: 50%; top: 40px; width: 80px; height: 5px; margin-left: -40px; background: var(--orange); }

  .hero { position: absolute; left: 0; top: 138px; width: 1200px; height: 587px; overflow: hidden; }
  .hero-photo { position: absolute; inset: 0;
    background:
      radial-gradient(ellipse 140px 210px at 1005px 330px, rgba(255,255,255,0.95) 0%, rgba(150,240,250,0.8) 40%, rgba(31,196,217,0.35) 70%, rgba(31,196,217,0) 100%),
      radial-gradient(ellipse 420px 360px at 900px 300px, rgba(31,196,217,0.45), rgba(31,196,217,0) 100%),
      linear-gradient(100deg, var(--sky-deep) 0%, var(--sky-mid) 45%, #0a8ab8 70%, var(--sky-deep) 100%);
  }
  .hero-copy { position: absolute; left: 0; top: 0; width: 1200px; height: 100%; text-align: center; color: var(--white); }
  .hero-kicker { position: absolute; left: 0; width: 1200px; top: 148px; margin-left: 24px; font-family: "Archivo Narrow", sans-serif; font-weight: 700; font-size: 38px; text-shadow: 0 2px 4px rgba(0,0,0,0.45); }
  .hero-divider { position: absolute; left: 402px; top: 208px; width: 426px; height: 56px; }
  .hero-title { position: absolute; left: 0; width: 1200px; top: 276px; margin-left: 24px; font-family: "Arimo", sans-serif; font-weight: 700; font-size: 66px; letter-spacing: -1px; text-shadow: 0 3px 5px rgba(0,0,0,0.45); }
  .hero-button { position: absolute; left: 554px; top: 452px; width: 117px; height: 33px; background: var(--navy); color: var(--white); font-family: "Arimo", sans-serif; font-weight: 400; font-size: 15px; line-height: 33px; padding-left: 16px; text-align: left; text-decoration: none; }
  .hero-button::after { content: ""; position: absolute; right: 0; bottom: 0; border-style: solid; border-width: 0 0 13px 13px; border-color: transparent transparent var(--orange) transparent; }

  .about { position: absolute; left: 0; top: 725px; width: 1200px; height: 176px; background: var(--mist); }
  .about-title { position: absolute; left: 0; width: 1200px; top: 100px; text-align: center; font-weight: 300; font-size: 42px; letter-spacing: 4px; color: var(--navy); text-transform: uppercase; }
</style>
</head>
<body>
  <header class="site-header">
    <div class="brand">
      <span class="brand-mark"></span>
      <span class="brand-name">Corvane Partners</span>
    </div>
    <nav class="main-nav">
      <a class="nav-item is-active" href="#" style="left:504px">Home</a>
      <a class="nav-item" href="#" style="left:623px">About us</a>
      <a class="nav-item" href="#" style="left:743px">Works</a>
      <a class="nav-item" href="#" style="left:869px">Services</a>
      <a class="nav-item" href="#" style="left:961px">Blog</a>
      <a class="nav-item" href="#" style="left:1053px">Contact</a>
    </nav>
  </header>

  <section class="hero">
    <div class="hero-photo" role="img" aria-label="Photograph of hanging light bulbs on a blue background, one glowing brightly on the right"></div>
    <div class="hero-copy">
      <h1 class="hero-kicker">FINANCIAL SOLUTION</h1>
      <svg class="hero-divider" viewBox="0 0 426 56" aria-hidden="true">
        <line x1="0" y1="28" x2="183" y2="28" stroke="#ffffff" stroke-width="1"/>
        <line x1="244" y1="28" x2="426" y2="28" stroke="#ffffff" stroke-width="1"/>
        <polygon points="213,2 239,28 213,54 187,28" fill="#f0a033"/>
        <text x="213" y="34" text-anchor="middle" fill="#ffffff" font-family="Arimo, sans-serif" font-weight="700" font-size="17">for</text>
      </svg>
      <p class="hero-title">Your Business</p>
      <a class="hero-button" href="#">View detail</a>
    </div>
  </section>

  <section class="about">
    <h2 class="about-title">A little about us</h2>
  </section>
</body>
</html>
```